Book Cover Design 'Boundless Tide - Lessons In Inner Sovereignty'

I need to see pitches / artwork for a book cover for new book designed to start a new global spiritual movement and save humanity. The book merges science and spirituality and explains to the reader why they are an all powerful god.

```html
<!DOCTYPE html>
<html lang="en">
<head>
<meta charset="utf-8">
<title>Boundless Tide – Book Cover</title>
<link rel="stylesheet" href="https://fonts.googleapis.com/css2?family=League+Gothic&family=Montserrat:wght@500&display=swap">
<style>
  :root {
    --page-bg: #ffffff;
    --ink-white: #ffffff;
    --ink-gold: #c7a57a;
    --glow-core: #f3dcff;
    --violet-bright: #a468e0;
    --violet-mid: #6a2f9c;
    --violet-deep: #361456;
    --night: #0b0a2c;
  }
  * { margin: 0; padding: 0; box-sizing: border-box; }
  html, body {
    width: 1200px;
    height: 1200px;
    overflow: hidden;
    background: var(--page-bg);
  }
  .canvas {
    position: relative;
    width: 1200px;
    height: 1200px;
  }
  .book-cover {
    position: absolute;
    left: 222px;
    top: 32px;
    width: 763px;
    height: 1142px;
    overflow: hidden;
    background: var(--night);
  }
  .cover-art {
    position: absolute;
    inset: 0;
    background:
      radial-gradient(circle at 50% 37%, var(--glow-core) 0%, #c58cf0 6%, var(--violet-bright) 16%, var(--violet-mid) 38%, var(--violet-deep) 62%, transparent 85%),
      linear-gradient(180deg, #3a1660 0%, #4a1e78 45%, #2a1050 68%, var(--night) 88%, var(--night) 100%);
  }
  .author-name {
    position: absolute;
    top: 48px;
    left: 0;
    width: 100%;
    text-align: center;
    font-family: "Montserrat", sans-serif;
    font-weight: 500;
    font-size: 42px;
    letter-spacing: 1px;
    color: var(--ink-white);
  }
  .book-title {
    position: absolute;
    inset: 0;
    font-family: "League Gothic", sans-serif;
    font-weight: 400;
    color: var(--ink-white);
  }
  .title-line {
    position: absolute;
    left: 0;
    width: 100%;
    text-align: center;
    white-space: nowrap;
    font-size: 214px;
    line-height: 1;
    letter-spacing: 2px;
  }
  .title-line--first { top: 634px; }
  .title-line--second { top: 810px; }
  .book-subtitle {
    position: absolute;
    top: 1046px;
    left: 0;
    width: 100%;
    text-align: center;
    white-space: nowrap;
    font-family: "Montserrat", sans-serif;
    font-weight: 500;
    font-size: 30px;
    letter-spacing: 1.5px;
    color: var(--ink-gold);
  }
</style>
</head>
<body>
  <main class="canvas">
    <section class="book-cover">
      <div class="cover-art" role="img" aria-label="Abstract purple light tunnel of glowing blocks rushing toward a bright central point"></div>
      <p class="author-name">AUTHOR NAME</p>
      <h1 class="book-title">
        <span class="title-line title-line--first">BOUNDLESS</span>
        <span class="title-line title-line--second">TIDE</span>
      </h1>
      <p class="book-subtitle">LESSONS IN INNER SOVEREIGNTY</p>
    </section>
  </main>
</body>
</html>
```